"Sun On Water" Gospel Presentation Booklet

I need a design for a 12 page (including front/back cover) square booklet, with religious images and aesthetically pleasing fonts/designs. I want it to be very simple, and very straightforward. The main focus of the project is it's content. So the design should be very nice, but also should point to the content, not take away from it, or create distraction. People should be more focused on the words than the imagery.

I enjoy modern designs, I need a sharp aesthetic that is clean and neat. Nothing over the top.
I have attached a word document with the content I would like on the pages.

Colors
0592cd
0255a3
33a6d7
85cae6
85acd3
3276b5
9bcb3b
f04a50
f68d4c

Requirements
Should not have
• Super feminine colors/aesthetics

```html
<!DOCTYPE html>
<html lang="en">
<head>
<meta charset="UTF-8">
<title>Sun On Water – Booklet Spread</title>
<link href="https://fonts.googleapis.com/css2?family=Kreon:wght@300;400&display=swap" rel="stylesheet">
<style>
  :root {
    --backdrop: #dcdcdc;
    --paper: #f7f7f7;
    --fold-shade: #e4e4e4;
    --sky-deep: #2e4a73;
    --sky-mid: #5c7690;
    --cloud-glow: #d8c79a;
    --cloud-light: #b9c3c6;
    --dawn-light: #fbe9a6;
    --dawn-gold: #f0b348;
    --dawn-amber: #c9733a;
    --dusk-red: #7a3331;
    --dusk-deep: #4a2a2e;
    --title-ink: #ffffff;
  }
  * { box-sizing: border-box; margin: 0; padding: 0; }
  html, body {
    width: 1200px;
    height: 900px;
    overflow: hidden;
    background: var(--backdrop);
  }
  .canvas {
    position: relative;
    width: 1200px;
    height: 900px;
    background: var(--backdrop);
  }
  .spread {
    position: absolute;
    left: 80px;
    top: 190px;
    width: 1040px;
    height: 520px;
    display: flex;
    box-shadow: 0 10px 30px rgba(0,0,0,0.12);
  }
  .page {
    position: relative;
    width: 520px;
    height: 520px;
    background: var(--paper);
    padding: 14px;
  }
  .page--left { padding-right: 0; border-right: 1px solid var(--fold-shade); }
  .page--right { padding-left: 0; }
  .page__photo {
    width: 100%;
    height: 100%;
  }
  .photo--clouds {
    background:
      radial-gradient(ellipse 35% 40% at 55% 45%, var(--cloud-glow) 0%, rgba(216,199,154,0) 70%),
      radial-gradient(ellipse 45% 55% at 50% 70%, var(--cloud-light) 0%, rgba(185,195,198,0) 75%),
      linear-gradient(160deg, var(--sky-deep) 0%, var(--sky-mid) 55%, var(--sky-deep) 100%);
  }
  .photo--summit {
    background:
      radial-gradient(ellipse 60% 35% at 40% 10%, var(--dawn-light) 0%, rgba(251,233,166,0) 80%),
      linear-gradient(180deg, var(--dawn-gold) 0%, var(--dawn-amber) 40%, var(--dusk-red) 72%, var(--dusk-deep) 100%);
  }
  .page__title {
    position: absolute;
    left: 0;
    right: 14px;
    top: 372px;
    text-align: center;
    font-family: "Kreon", Georgia, serif;
    font-weight: 300;
    font-size: 38px;
    letter-spacing: 0.5px;
    color: var(--title-ink);
  }
</style>
</head>
<body>
  <main class="canvas">
    <section class="spread">
      <article class="page page--left">
        <div class="page__photo photo--clouds" role="img" aria-label="Sunbeams breaking through clouds in a deep blue sky"></div>
      </article>
      <article class="page page--right">
        <div class="page__photo photo--summit" role="img" aria-label="Silhouette of a person with outstretched arms on a mountain top at golden sunrise"></div>
        <h1 class="page__title">Sun On Water...</h1>
      </article>
    </section>
  </main>
</body>
</html>
```